Morvela Drinks LLC website and online trading portal

Beverage Manufacturing company needs a website design. Should include 5 main pages. Home, Products, About, FAQ and Contact Us. Should also include a shopping cart, online order and shipping page. Company logo is attached.

Target Market(s)

General Public, health conscious individuals

Font styles to use
Serif
Sans Serif
Script

Colors
abd037
fbee3e
ffc214
ffffff

Requirements
Must have
• e-commerce site with 5 main pages. Home, Products, About, FAQ and Contact Us. Should also include a shopping cart, online order and shipping page. Coloscheme should be derived from attached logo

```html
<!DOCTYPE html>
<html lang="en">
<head>
<meta charset="UTF-8">
<title>Morvela Drinks — Natural Refreshments</title>
<link href="https://fonts.googleapis.com/css2?family=Great+Vibes&family=Arimo:wght@400;700&family=Open+Sans:wght@400;600;700&display=swap" rel="stylesheet">
<style>
:root{
  --green-dark:#2f8a1d;
  --green:#4ea523;
  --lime:#abd037;
  --lemon:#fbee3e;
  --amber:#ffc214;
  --orange:#f7941d;
  --orange-deep:#ff7f14;
  --white:#ffffff;
  --ink:#2b2b2b;
  --grey:#555555;
  --soft:#f4f4f4;
}
*{margin:0;padding:0;box-sizing:border-box}
html,body{width:1200px;height:3743px;overflow:hidden;background:var(--white)}
body{position:relative;font-family:"Open Sans",Arial,sans-serif;color:var(--ink)}
.abs{position:absolute}
.script{font-family:"Great Vibes",cursive;font-weight:400}
.heading{font-family:"Arimo",Arial,sans-serif;font-weight:700}
.photo{position:absolute}

/* header */
.site-header{position:absolute;left:0;top:0;width:1200px;height:121px;background:linear-gradient(180deg,#6cbb2f 0%,var(--green-dark) 100%)}
.brand{position:absolute;left:102px;top:38px;display:flex;align-items:center;gap:12px}
.brand-dot{width:52px;height:52px;border-radius:50%;background:var(--amber)}
.brand-name{font-family:"Open Sans",sans-serif;font-weight:700;font-size:24px;color:var(--white)}
.nav a{position:absolute;top:62px;font-family:"Arimo",Arial,sans-serif;font-size:13px;color:var(--white);text-decoration:none;letter-spacing:.3px}
.nav .active::after{content:"";position:absolute;left:2px;right:2px;top:22px;height:2px;border-radius:2px;background:var(--white)}
.cart{position:absolute;left:1016px;top:54px}
.cart-count{position:absolute;left:1040px;top:52px;width:14px;height:14px;border-radius:50%;background:var(--amber);color:var(--white);font-size:9px;text-align:center;line-height:14px;font-weight:700}

/* hero */
.hero{position:absolute;left:0;top:121px;width:1200px;height:601px;background:linear-gradient(180deg,#f2f2f2,#e2e2e2 60%,#f4f4f4)}
.hero-title{position:absolute;left:164px;top:162px;font-size:96px;line-height:1;color:var(--green)}
.hero-sub{position:absolute;left:168px;top:290px;font-size:29px;color:var(--orange-deep);letter-spacing:.2px}
.hero-text{position:absolute;left:170px;top:341px;width:400px;font-size:13.5px;line-height:24px;color:var(--grey)}
.btn-solid{position:absolute;display:flex;align-items:center;justify-content:center;border-radius:30px;background:var(--lime);color:var(--white);font-family:"Arimo",Arial,sans-serif;font-weight:700;font-size:16px}
.hero-dots span{position:absolute;left:51px;width:13px;height:13px;border-radius:50%;background:#6a6a6a}
.hero-dots span.ring{background:transparent;border:2px solid #6a6a6a}

/* about */
.about{position:absolute;left:0;top:722px;width:1200px;height:491px;background:var(--white)}
.eyebrow{font-size:46px;color:var(--green);line-height:1}
.section-title{font-size:33px;color:var(--ink);letter-spacing:.3px}
.copy{font-size:14px;line-height:25px;color:var(--grey)}
.btn-line{position:absolute;display:flex;align-items:center;justify-content:center;border:2px solid var(--orange);border-radius:30px;color:var(--orange);font-family:"Arimo",Arial,sans-serif;font-weight:700;font-size:15px}

/* benefits */
.benefits{position:absolute;left:0;top:1213px;width:1200px;height:550px;background:linear-gradient(90deg,#f6f6f6,#ececec)}

/* products */
.products{position:absolute;left:0;top:1763px;width:1200px;height:614px;background:linear-gradient(100deg,var(--orange-deep) 0%,var(--amber) 55%,var(--lemon) 100%)}
.products .eyebrow{color:var(--white);position:absolute;left:0;width:1200px;text-align:center;top:28px;font-size:44px}
.products .section-title{color:var(--white);position:absolute;left:0;width:1200px;text-align:center;top:78px;font-size:29px}
.product{position:absolute;top:144px;width:240px;text-align:center;color:var(--white)}
.product .bottle{margin:0 auto;width:80px;height:280px;border-radius:26px 26px 14px 14px}
.product .name{margin-top:16px;font-size:19px}
.product .price{margin-top:4px;font-size:19px}
.product .shop{margin:12px auto 0;width:122px;height:38px;border:2px solid var(--white);border-radius:20px;font-family:"Arimo",Arial,sans-serif;font-weight:700;font-size:12px;line-height:34px}

/* reviews */
.reviews{position:absolute;left:0;top:2377px;width:1200px;height:449px;background:#fafafa}
.review{position:absolute;top:148px;width:412px;height:214px;background:var(--white);box-shadow:0 2px 10px rgba(0,0,0,.08);text-align:center}
.stars{margin-top:38px;color:var(--amber);font-size:22px;letter-spacing:4px}
.review p{margin:14px auto 0;width:350px;font-size:13px;line-height:23px;color:#888}
.review .author{margin-top:14px;font-family:"Arimo",Arial,sans-serif;font-weight:700;font-size:12px;color:var(--ink)}
.pager span{position:absolute;top:2774px;width:11px;height:11px;border-radius:50%;border:1.5px solid #999}
.pager span.on{background:var(--orange);border-color:var(--orange)}

/* faq */
.faq{position:absolute;left:0;top:2826px;width:1200px;height:535px;background:var(--white)}
.faq-title{position:absolute;left:150px;top:103px;font-size:25px;color:var(--lime);letter-spacing:.3px}
.q{position:absolute;left:151px;width:446px;font-size:16.5px;font-weight:600;color:var(--ink);display:flex;justify-content:space-between}
.q b{color:var(--lime);font-size:24px;font-weight:400;line-height:20px}
.answer{position:absolute;left:151px;top:208px;width:440px;font-size:13px;line-height:19px;color:var(--grey)}

/* footer */
.site-footer{position:absolute;left:0;top:3361px;width:1200px;height:382px;background:linear-gradient(180deg,#86c13a 0%,var(--lime) 100%);color:var(--white)}
.foot-brand{position:absolute;left:140px;top:82px;display:flex;flex-direction:column;align-items:center;gap:10px;width:200px}
.foot-brand .brand-dot{width:64px;height:64px}
.foot-head{position:absolute;font-family:"Arimo",Arial,sans-serif;font-weight:700;font-size:15px;letter-spacing:.2px}
.foot-links{position:absolute;left:396px;top:110px;list-style:none;font-size:13px;line-height:22.5px}
.email{position:absolute;left:577px;top:104px;width:263px;height:39px;border-radius:20px;background:var(--white);display:flex;align-items:center;padding-left:22px;gap:10px;font-size:11px;color:#888}
.subscribe{position:absolute;left:583px;top:156px;width:143px;height:40px;border-radius:20px;background:var(--amber);display:flex;align-items:center;justify-content:center;font-family:"Arimo",Arial,sans-serif;font-weight:700;font-size:13px}
.social span{position:absolute;top:120px;width:16px;height:16px;border-radius:50%;background:var(--white)}
.copyright{position:absolute;left:0;top:329px;width:1200px;text-align:center;font-size:11px}
</style>
</head>
<body>

<header class="site-header">
  <div class="brand"><span class="brand-dot"></span><span class="brand-name">Morvela Drinks</span></div>
  <nav class="nav">
    <a class="active" style="left:474px">HOME</a>
    <a style="left:559px">PRODUCTS</a>
    <a style="left:680px">ABOUT</a>
    <a style="left:771px">FAQ</a>
    <a style="left:847px">CONTACT US</a>
  </nav>
  <svg class="cart" width="28" height="26" viewBox="0 0 28 26" fill="none" stroke="#fff" stroke-width="2" stroke-linecap="round" stroke-linejoin="round">
    <path d="M2 3h4l3 13h13l3-9H8"/><circle cx="11" cy="21" r="2"/><circle cx="21" cy="21" r="2"/>
  </svg>
  <span class="cart-count">0</span>
</header>

<section class="hero">
  <div class="photo" role="img" aria-label="Snowy mountain landscape backdrop" style="left:0;top:0;width:1200px;height:601px;background:linear-gradient(160deg,#f7f7f7 0%,#dcdcdc 45%,#f0f0f0 100%)"></div>
  <div class="photo" role="img" aria-label="Green leafy branch" style="left:0;top:10px;width:245px;height:145px;background:radial-gradient(ellipse at 50% 50%,#5fb33a 0%,#8dc63f 45%,rgba(141,198,63,0) 72%)"></div>
  <div class="photo" role="img" aria-label="Three bottles of ginger juice with green apples and leaves" style="left:567px;top:68px;width:479px;height:479px;background:radial-gradient(ellipse at 50% 55%,#f7a21b 0%,#f6c23a 30%,#9ccf3c 55%,rgba(230,230,230,0) 75%)"></div>
  <div class="hero-title script">Morvela Drinks</div>
  <div class="hero-sub heading">NATURAL REFRESHMENTS</div>
  <p class="hero-text">Augiat in pede Fusce tellus Sed metus augue convallis et vehicula ut pulvinar eu ante Integer orci tellus</p>
  <a class="btn-solid" style="left:168px;top:405px;width:201px;height:49px">ONLINE ORDER</a>
  <div class="hero-dots">
    <span class="ring" style="top:251px"></span>
    <span style="top:270px"></span>
    <span style="top:290px"></span>
    <span style="top:309px"></span>
  </div>
</section>

<section class="about">
  <div class="photo" role="img" aria-label="Smiling woman drinking a glass of orange juice" style="left:145px;top:19px;width:429px;height:472px;background:linear-gradient(180deg,#e9e3de 0%,#d9c2b0 55%,#b9d3dc 100%)"></div>
  <div class="abs eyebrow script" style="left:660px;top:68px">About</div>
  <h2 class="abs section-title heading" style="left:661px;top:120px">MORVELA DRINKS</h2>
  <p class="abs copy" style="left:662px;top:176px;width:420px">Praesent elementum elit at tellus Curabitur metus ipsum luctus eu malesuada ut tincidunt sed diam</p>
  <p class="abs copy" style="left:662px;top:238px;width:450px">Maecenas aliquet velit vel turpis Mauris neque metus malesuada nec ultricies sit amet porttitor mattis enim In massa libero interdum nec interdum vel blandit sed nulla</p>
  <a class="btn-line" style="left:661px;top:340px;width:170px;height:47px">LEARN MORE</a>
</section>

<section class="benefits">
  <div class="photo" role="img" aria-label="Pineapple pieces scattered on a light surface" style="left:0;top:0;width:200px;height:150px;background:radial-gradient(ellipse at 40% 40%,#f8d64a 0%,rgba(248,214,74,0) 70%)"></div>
  <div class="photo" role="img" aria-label="Juice bottles with green apples, oranges in a basket and tea on a bamboo mat" style="left:567px;top:0;width:633px;height:550px;background:linear-gradient(120deg,rgba(236,236,236,0) 0%,#d9e9b2 25%,#f6b73a 55%,#c9a273 80%,#f39a2a 100%)"></div>
  <div class="abs eyebrow script" style="left:144px;top:112px;font-size:40px">Benefits of Ginger</div>
  <h2 class="abs section-title heading" style="left:148px;top:164px;font-size:32px">WHY OUR JUICES</h2>
  <p class="abs copy" style="left:148px;top:217px;width:410px">Praesent elementum elit at tellus Curabitur metus ipsum luctus eu malesuada ut tincidunt sed diam</p>
  <p class="abs copy" style="left:148px;top:280px;width:410px">Maecenas aliquet velit vel turpis Mauris neque metus malesuada nec ultricies sit amet porttitor mattis enim In massa libero interdum nec interdum vel</p>
  <a class="btn-line" style="left:145px;top:384px;width:170px;height:45px">LEARN MORE</a>
</section>

<section class="products">
  <div class="eyebrow script">Product</div>
  <h2 class="section-title heading">OUR JUICES</h2>
  <div class="product" style="left:112px">
    <div class="bottle" role="img" aria-label="Orange ginger juice bottle" style="background:linear-gradient(180deg,#f6a51c,#f7c62c 60%,#f2d06b)"></div>
    <div class="name">Your Juice Title here</div><div class="price">$25.99</div><div class="shop">SHOP NOW</div>
  </div>
  <div class="product" style="left:358px">
    <div class="bottle" role="img" aria-label="Lime ginger juice bottle" style="background:linear-gradient(180deg,#6fd42c,#9de346 60%,#c9e77a)"></div>
    <div class="name">Your Juice Title here</div><div class="price">$25.99</div><div class="shop">SHOP NOW</div>
  </div>
  <div class="product" style="left:606px">
    <div class="bottle" role="img" aria-label="Mint ginger juice bottle" style="background:linear-gradient(180deg,#3fd87a,#69e2a0 60%,#b8ead0)"></div>
    <div class="name">Your Juice Title here</div><div class="price">$25.99</div><div class="shop">SHOP NOW</div>
  </div>
  <div class="product" style="left:854px">
    <div class="bottle" role="img" aria-label="Berry ginger juice bottle" style="background:linear-gradient(180deg,#e8263a,#ef4a5c 60%,#f3a0a6)"></div>
    <div class="name">Your Juice Title here</div><div class="price">$25.99</div><div class="shop">SHOP NOW</div>
  </div>
</section>

<section class="reviews">
  <div class="abs eyebrow script" style="left:0;width:1200px;text-align:center;top:38px;font-size:44px;color:var(--ink)">Reviews</div>
  <h2 class="abs heading" style="left:0;width:1200px;text-align:center;top:88px;font-size:24px;color:var(--ink)">WHAT PEOPLE SAYS</h2>
  <article class="review" style="left:174px">
    <div class="stars">★★★★★</div>
    <p>Maecenas aliquet velit vel turpis Mauris neque metus malesuada nec ultricies sit amet porttitor mattis enim In massa libero interdum nec interdum vel</p>
    <div class="author">BY AUTHOR NAME</div>
  </article>
  <article class="review" style="left:609px">
    <div class="stars">★★★★★</div>
    <p>Maecenas aliquet velit vel turpis Mauris neque metus malesuada nec ultricies sit amet porttitor mattis enim In massa libero interdum nec interdum vel</p>
    <div class="author">BY AUTHOR NAME</div>
  </article>
</section>
<div class="pager">
  <span style="left:577px"></span>
  <span class="on" style="left:595px"></span>
  <span style="left:613px"></span>
</div>

<section class="faq">
  <h2 class="faq-title heading">FREQUENTLY ASKED QUESTIONS</h2>
  <div class="q" style="top:164px">Donec convallis pede venenatis?<b>-</b></div>
  <p class="answer">parturient montes nascetur ridiculus mus In iaculis facilisis massa Etiam eu urna Sed porta Suspendisse quam leo molestie</p>
  <div class="q" style="top:268px">Nunc tempus felis vitae urna Vivamus porttitor ?<b>+</b></div>
  <div class="q" style="top:331px">Curabitur iaculis tempus eros?<b>+</b></div>
  <div class="q" style="top:393px">Morbi eget arcu Morbi porta libero ?<b>+</b></div>
  <div class="photo" role="img" aria-label="Juice bottle surrounded by pineapple, apple and ginger in a round green frame" style="left:647px;top:55px;width:396px;height:416px;border-radius:50%;background:radial-gradient(circle at 50% 50%,#f6c22b 0%,#9ccf3c 45%,#4ea523 70%,#f5b51c 72%,#abd037 100%)"></div>
</section>

<footer class="site-footer">
  <div class="foot-brand"><span class="brand-dot"></span><span class="brand-name">Morvela Drinks</span></div>
  <div class="foot-head" style="left:392px;top:74px">QUICK LINKS</div>
  <ul class="foot-links">
    <li>About Us</li><li>Product</li><li>FAQ</li><li>Cart</li><li>Contact Us</li>
  </ul>
  <div class="foot-head" style="left:583px;top:74px">SIGN UP FOR UPDATES</div>
  <div class="email">
    <svg width="16" height="12" viewBox="0 0 16 12" fill="none" stroke="#999" stroke-width="1.2"><rect x="1" y="1" width="14" height="10"/><path d="M1 1l7 6 7-6"/></svg>
    Email address
  </div>
  <div class="subscribe">SUBSCRIBE</div>
  <div class="foot-head" style="left:899px;top:80px">GET IN TOUCH</div>
  <div class="social" aria-label="Social links">
    <span style="left:897px"></span>
    <span style="left:945px"></span>
    <span style="left:993px"></span>
    <span style="left:1041px"></span>
  </div>
  <div class="copyright">© 2020 Company Name  All right reserved</div>
</footer>

</body>
</html>
```